New Zealand Export company needs business cards

We need new business cards to match our new logo for a company based in New Zealand who deal specifically with the Pacific Islands. We source, consolidate and ship products out of New Zealand to the Pacific Islands. Will attach our old ones and also new logo.
Would like the Islands we deal with and the areas of work we have access to, to be included on the business cards.

Contact Information for Business Card

T +64 9 571 3048
F +64 9 571 6285
12-18 Kowhai Lane, Drury, 2113
PO Box 814, Drury, Auckland 2247, New Zealand
www.falconfreight.example.nz
E sales@falconfreight.example.nz

Font styles to use
Sans Serif

Colors
85abd2
33a6d7
ffffff

Requirements
Must have
• A company of PWM

```html
<!DOCTYPE html>
<html lang="en">
<head>
<meta charset="utf-8">
<title>Falcon Freight – Business Cards</title>
<link rel="stylesheet" href="https://fonts.googleapis.com/css2?family=Lato:wght@400;700&display=swap">
<style>
  :root {
    --bg: #2a2a2a;
    --card-light: #eeeeee;
    --brand-blue: #1a5aa8;
    --brand-sky: #33a6d7;
    --brand-soft: #85abd2;
    --text-grey: #3c3c3c;
    --rule-grey: #8a8a8a;
    --white: #ffffff;
  }
  * { margin: 0; padding: 0; box-sizing: border-box; }
  html, body { width: 1200px; height: 1200px; overflow: hidden; background: var(--bg); }
  body { font-family: "Lato", sans-serif; }
  .stage { position: relative; width: 1200px; height: 1200px; }

  .card { position: absolute; top: 310px; height: 594px; box-shadow: 0 4px 12px rgba(0,0,0,.55); }
  .card--front { left: 234px; width: 364px; background: var(--card-light); color: var(--text-grey); text-align: center; }
  .card--back {
    left: 627px; width: 369px; color: var(--white); text-align: center;
    background: radial-gradient(ellipse at 55% 45%, #3fc0ea 0%, var(--brand-sky) 35%, #1f78c4 70%, #1457a6 100%);
  }

  .wordmark { position: absolute; left: 0; right: 0; top: 124px; display: flex; justify-content: center; align-items: center; gap: 12px; color: var(--brand-blue); font-weight: 700; }
  .wordmark__square { width: 14px; height: 14px; background: var(--brand-blue); }
  .wordmark__text { font-size: 30px; line-height: 1; letter-spacing: 1px; text-align: left; }
  .wordmark__text span { display: block; font-size: 17px; letter-spacing: 5px; margin-top: 6px; }

  .person { position: absolute; left: 0; right: 0; top: 284px; }
  .person__name { font-size: 22px; font-weight: 700; color: var(--brand-blue); line-height: 1.1; }
  .person__role { font-size: 17px; margin-top: 3px; }

  .icon-row { position: absolute; left: 78px; right: 73px; top: 347px; display: flex; align-items: center; gap: 5px; }
  .icon-row__rule { flex: 1; height: 1px; background: var(--rule-grey); }
  .icon-row__icon { width: 23px; height: 23px; border-radius: 5px; background: var(--brand-blue); display: flex; align-items: center; justify-content: center; }

  .contact { position: absolute; left: 0; right: 0; top: 376px; font-size: 17px; line-height: 21.6px; }
  .rule { position: absolute; left: 78px; right: 73px; top: 473px; height: 1px; background: var(--rule-grey); }
  .address { position: absolute; left: 0; right: 0; top: 484px; font-size: 17px; line-height: 21.6px; }

  .back-wordmark { position: absolute; left: 0; right: 0; top: 256px; font-weight: 700; }
  .back-wordmark__name { font-size: 50px; letter-spacing: 2px; line-height: 1; }
  .back-wordmark__sub { font-size: 26px; letter-spacing: 10px; margin-top: 8px; }
  .parent-line { position: absolute; left: 0; right: 0; top: 524px; font-size: 19px; font-weight: 400; }
</style>
</head>
<body>
<main class="stage">
  <section class="card card--front">
    <div class="wordmark">
      <div class="wordmark__square"></div>
      <div class="wordmark__text">FALCON<span>FREIGHT</span></div>
    </div>

    <div class="person">
      <div class="person__name">DANIEL HARPER</div>
      <div class="person__role">Managing Director</div>
    </div>

    <div class="icon-row">
      <div class="icon-row__rule"></div>
      <div class="icon-row__icon" aria-label="Phone">
        <svg width="15" height="15" viewBox="0 0 16 16"><path d="M3 2h3l1 3-2 1a8 8 0 0 0 5 5l1-2 3 1v3a1 1 0 0 1-1 1A12 12 0 0 1 2 3a1 1 0 0 1 1-1z" fill="#fff"/></svg>
      </div>
      <div class="icon-row__icon" aria-label="Fax">
        <svg width="15" height="15" viewBox="0 0 16 16" fill="#fff"><rect x="4" y="1" width="8" height="4"/><rect x="1" y="6" width="14" height="6" rx="1"/><rect x="4" y="10" width="8" height="5" fill="#fff" stroke="#1a5aa8" stroke-width="1"/></svg>
      </div>
      <div class="icon-row__icon" aria-label="Email">
        <svg width="15" height="15" viewBox="0 0 16 16"><rect x="1" y="3" width="14" height="10" fill="#fff"/><path d="M1 3l7 6 7-6" fill="none" stroke="#1a5aa8" stroke-width="1.3"/></svg>
      </div>
      <div class="icon-row__icon" aria-label="Website">
        <svg width="15" height="15" viewBox="0 0 16 16"><circle cx="8" cy="8" r="6.5" fill="#fff"/><path d="M1.5 8h13M8 1.5c-3 3.5-3 9.5 0 13M8 1.5c3 3.5 3 9.5 0 13" fill="none" stroke="#1a5aa8" stroke-width="1"/></svg>
      </div>
      <div class="icon-row__rule"></div>
    </div>

    <div class="contact">
      +64 9 571 3048<br>
      +64 9 571 6285<br>
      sales@falconfreight.example.nz<br>
      www.falconfreight.example.nz
    </div>
    <div class="rule"></div>
    <div class="address">
      12-18 Kowhai Lane, Drury, 2113<br>
      PO Box 814, Drury, Auckland 2247<br>
      New Zealand
    </div>
  </section>

  <section class="card card--back">
    <div class="back-wordmark">
      <div class="back-wordmark__name">FALCON</div>
      <div class="back-wordmark__sub">FREIGHT</div>
    </div>
    <div class="parent-line">A COMPANY OF PWM</div>
  </section>
</main>
</body>
</html>
```